House Cleaning Platform for Consumers and Cleaners

UPDATE: I've attached screenshots showing a purchase flow example, something all designers have missed in their designs. PLEASE check the URLs I've included in the brief for examples of a cleaning website. I've seen mostly landing pages and nothing else.

WHAT I'M LOOKING FOR:
I need the UI designed for a house cleaning web platform from 2 separate experiences: one from the consumer end to order a cleaner to come clean their house and one from a cleaner’s end that manages their orders and manages their schedule.

The UI will need to include photo uploading for before and after photos, a checkout/cart experience w/ tips, toggle options for adding and removing rooms/extras cleaning add-ons, customer+cleaner reviews (meaning the cleaner finished the job and they can rate and review the customer as well as the customer can rate and review the cleaner), order history for consumers, job history for cleaners, profile, settings, and landing pages for both.

PLEASE DO NOT USE THE COLOR BLUE AS THE PRIMARY COLOR. Use a light green (HEX #2fdf86) instead for primary theming color.

REFERENCES:
If you'd like a few websites I've enjoyed for references, checkout:
larkhollowhome.example, vomrix.example, and pebblerunhomes.example.

For sake of branding, the company name is BrimNest. Currently do not have a logo as we have not decided on the name. Logo will come later.

Feel free to reach out to me if you have any questions!
Updates

Most designer submissions were a landing page and only a landing page. Very few designed the flows I requested and none designed a schedule management page. I even updated the Brief to more clearly outline the needs and references. Only about 2-3 of the designers actually did more than a landing page. Still don't believe I received 6 designers input that I had paid for.

Target Market(s)

FULL-TIME WORKING HOUSEHOLDS, SINGLE PROFESSIONALS, SINGLE PARENTS, ELDERLY & MOBILITY CHALLENGED, BUSY BODIES.

Industry/Entity Type

Cleaning, gig work.

Number of Pages Required

5+ page

Font styles to use
Other font styles liked:
• Jost or Lexend are great Google Font options I've used in the pitch deck and horribly done app mockups.

Colors
00AB8E
00BBA5
67D7C9
C6EFE9
E9F9F6
59FF00
82FF00
B8FF75
E3FFCB
F4FFEA
FFF300
FFF600
FEFA6F
FFFEC7
FFFEE8
FFC000
F8CF3A
FAE287
FDF2CF
FEFAEE

Requirements
Must have
• Landing page, consumer flow, cleaner schedule management, checkout flow, Rate & Review for consumer and/or cleaner, order history, profile.
Nice to have
• I'd like it to be simple in design and modern, but not so simple it's boring. Iconography can sometimes break that up, but I don't want it looking busy. It's a cleaning platform so the UI should look clean.

```html
<!DOCTYPE html>
<html lang="en">
<head>
<meta charset="utf-8">
<title>BrimNest – Book Your Services</title>
<link rel="stylesheet" href="https://fonts.googleapis.com/css2?family=Nunito:wght@400;500;600;700&family=Open+Sans:wght@400;500;700&display=swap">
<style>
  :root {
    --green: #2fdf86;
    --green-strong: #26d07d;
    --ink: #111111;
    --muted: #4a4a4a;
    --line: #cfcfcf;
    --bg: #ffffff;
  }
  * { box-sizing: border-box; margin: 0; padding: 0; }
  html, body { width: 1200px; height: 658px; overflow: hidden; background: var(--bg); }
  body { position: relative; font-family: "Nunito", sans-serif; color: var(--ink); }

  .brand {
    position: absolute; left: 102px; top: 17px;
    font-family: "Open Sans", sans-serif; font-weight: 700; font-size: 30px;
    color: var(--green); letter-spacing: -0.3px;
  }
  .nav { position: absolute; top: 27px; font-size: 11.5px; font-weight: 500; }
  .nav a { position: absolute; color: var(--ink); text-decoration: none; white-space: nowrap; }
  .search {
    position: absolute; left: 731px; top: 22.5px; width: 218px; height: 25px;
    border: 1px solid var(--line); border-radius: 13px;
  }
  .search svg { position: absolute; left: 7px; top: 5px; }
  .search span { position: absolute; left: 40px; top: 4.5px; font-size: 11.5px; font-weight: 500; }
  .login { position: absolute; left: 981px; top: 27px; font-size: 11.5px; font-weight: 500; }
  .signup {
    position: absolute; left: 1024px; top: 22.5px; width: 75px; height: 25px;
    background: var(--green-strong); border-radius: 13px;
    font-size: 11px; font-weight: 600; display: flex; align-items: center; justify-content: center;
  }

  .page-title {
    position: absolute; left: 0; right: 0; top: 126px; text-align: center;
    font-family: "Open Sans", sans-serif; font-weight: 700; font-size: 36px; padding-left: 4px;
  }
  .divider { position: absolute; left: 0; right: 0; top: 215px; border-top: 1px solid var(--green); }

  .question {
    position: absolute; left: 101px; top: 280px;
    font-family: "Open Sans", sans-serif; font-weight: 500; font-size: 19.5px;
  }
  .hint { position: absolute; left: 101px; top: 321px; font-size: 11.5px; color: var(--muted); }

  .option {
    position: absolute; width: 468px; height: 37px;
    border: 1px solid var(--line); border-radius: 2px;
    display: flex; align-items: center;
  }
  .option .radio {
    position: absolute; left: 18px; width: 13px; height: 13px; border-radius: 50%;
    border: 1px solid #c4c4c4;
  }
  .option .radio.selected { border: 3.5px solid var(--green-strong); }
  .option .label {
    position: absolute; left: 43px; font-family: "Open Sans", sans-serif; font-size: 11.5px; font-weight: 500;
  }
  .stepper {
    position: absolute; left: 375px; top: 5.5px; display: flex;
    border: 1px solid var(--line); height: 24px;
  }
  .stepper span {
    width: 25px; display: flex; align-items: center; justify-content: center;
    font-size: 11.5px; font-weight: 600;
  }
  .stepper span + span { border-left: 1px solid var(--line); }

  .btn {
    position: absolute; top: 514px; width: 175px; height: 49px; border-radius: 25px;
    display: flex; align-items: center; justify-content: center;
    font-size: 16px; font-weight: 600;
  }
  .btn-back { left: 101px; border: 1px solid var(--line); }
  .btn-next { left: 307.5px; background: var(--green-strong); }
</style>
</head>
<body>
  <header>
    <div class="brand">BrimNest</div>
    <nav class="nav">
      <a style="left:438px">Home</a>
      <a style="left:489px">Pricing</a>
      <a style="left:546px">Services</a>
      <a style="left:612px">Contact</a>
      <a style="left:674px">Help</a>
    </nav>
    <div class="search">
      <svg width="14" height="14" viewBox="0 0 14 14" fill="none" stroke="#111" stroke-width="1.1">
        <circle cx="6" cy="6" r="5"/><line x1="9.6" y1="9.6" x2="13" y2="13"/>
      </svg>
      <span>Search</span>
    </div>
    <div class="login">Login</div>
    <div class="signup">Sign Up</div>
  </header>

  <h1 class="page-title">Book Your Services Now</h1>
  <div class="divider"></div>

  <h2 class="question">Do You Want To Exclude Any Bathrooms Or Bedrooms?</h2>
  <p class="hint">If you don’t need some rooms to cleaned, indicate that below. Excluding room will be calculated into the quote.</p>

  <div class="option" style="left:101px; top:357.5px;">
    <span class="radio selected"></span>
    <span class="label">Exclude Bedroom(s)</span>
    <div class="stepper">
      <span><svg width="10" height="2"><line x1="0" y1="1" x2="10" y2="1" stroke="#aaa"/></svg></span>
      <span>1</span>
      <span><svg width="10" height="10"><path d="M5 0V10M0 5H10" stroke="#333"/></svg></span>
    </div>
  </div>
  <div class="option" style="left:630px; top:357.5px;">
    <span class="radio"></span>
    <span class="label">Exclude Bathroom(s)</span>
  </div>
  <div class="option" style="left:101px; top:414px;">
    <span class="radio"></span>
    <span class="label">Do not exclude any rooms</span>
  </div>

  <div class="btn btn-back">Back</div>
  <div class="btn btn-next">Save &amp; Next</div>
</body>
</html>
```